Marlowe Holdings LLC - Business Cards

Need the following information on the cards:

Name: Dean R Vossler
Title: Chief Executive Manager

Business address:
412 N Ridgeview Lane #118
Linden Falls, Il 60412

Phone: (555) 555-0148 - Business
KPV FFL license number: 5-21-xxx-xx-xx-04519
Email: dean.vossler@marloweholdingsffl.com

Target Market(s)

Firearm owners

Industry/Entity Type

Firearms industry,

Contact Information for Business Card

Contact number, name and title, web page address, email, business address and kpv license number,

Requirements
Must have
• Name, title, business address, phone numbers, KPV license numbers, web page address and email address.
Nice to have
• Cellphone number,

```html
<!DOCTYPE html>
<html lang="en">
<head>
<meta charset="utf-8">
<title>Marlowe Holdings LLC – Business Cards</title>
<link rel="stylesheet" href="https://fonts.googleapis.com/css2?family=Open+Sans:wght@400;600&family=Encode+Sans+Condensed:wght@400&family=Montserrat:wght@800&display=swap">
<style>
  :root {
    --brand-red: #d80000;
    --ink: #111111;
    --paper: #ffffff;
    --edge: #a8a8a8;
  }
  * { margin: 0; padding: 0; box-sizing: border-box; }
  html, body { width: 1200px; height: 1170px; overflow: hidden; background: var(--paper); }
  .sheet { position: relative; width: 1200px; height: 1170px; }
  .card {
    position: absolute; width: 572px; height: 349px;
    background: var(--paper); border: 1px solid var(--edge); overflow: hidden;
  }
  .card--red { background: var(--brand-red); border-color: var(--brand-red); }

  /* front side: brand name */
  .brand {
    position: absolute; inset: 0;
    display: flex; flex-direction: column; align-items: center; justify-content: center; gap: 18px;
  }
  .brand__dot { width: 120px; height: 120px; border: 4px solid var(--ink); border-radius: 50%; }
  .brand__name {
    font-family: "Montserrat", sans-serif; font-weight: 800; font-size: 30px;
    letter-spacing: 1px; color: var(--brand-red); text-align: center; line-height: 1.1;
  }

  .name { font-family: "Open Sans", sans-serif; font-weight: 600; font-size: 27px; line-height: 1; position: absolute; }
  .title { font-family: "Open Sans", sans-serif; font-weight: 400; font-size: 18px; line-height: 1; position: absolute; color: var(--ink); }
  .contact { font-family: "Encode Sans Condensed", sans-serif; font-size: 18px; line-height: 24px; position: absolute; color: var(--ink); }
  .centered { left: 0; right: 0; text-align: center; }

  /* back A: red */
  .card--red .name { color: var(--paper); top: 50px; }
  .rule-title {
    position: absolute; top: 108px; left: 0; right: 0;
    display: flex; justify-content: center; align-items: center; gap: 6px;
    font-family: "Open Sans", sans-serif; font-weight: 600; font-size: 18px;
    color: var(--paper); letter-spacing: 0.5px; line-height: 1;
  }
  .rule-title::before, .rule-title::after { content: ""; width: 38px; height: 2px; background: var(--paper); }
  .card--red .contact { color: var(--paper); top: 215px; line-height: 22px; font-size: 19px; }
  .card--red .license { top: 298px; font-size: 17px; }

  /* back B: band */
  .card--band .name { color: var(--brand-red); top: 42px; }
  .card--band .title { top: 76px; }
  .card--band .address { top: 136px; line-height: 24.5px; }
  .band { position: absolute; left: 0; top: 0; width: 572px; height: 349px; }
  .card--band .license { top: 260px; font-size: 16px; line-height: 22px; }

  /* back C: offset */
  .card--offset .name { color: var(--brand-red); top: 40px; right: 96px; }
  .card--offset .title { top: 72px; right: 96px; }
  .card--offset .address { left: 30px; top: 188px; line-height: 25px; }
  .accent-line { position: absolute; left: 32px; top: 294px; width: 322px; height: 4px; background: var(--brand-red); border-radius: 2px; }
  .card--offset .license { left: 30px; top: 303px; font-size: 14px; }
  .decor-area {
    position: absolute; left: 372px; top: 135px; width: 200px; height: 163px;
    background: linear-gradient(180deg, #fbe3e3 0%, #f3b3b3 100%);
    border-bottom: 4px solid var(--brand-red);
  }
</style>
</head>
<body>
<div class="sheet">

  <!-- Row 1 -->
  <section class="card" style="left:18px; top:23px;">
    <div class="brand"><span class="brand__dot"></span><span class="brand__name">MARLOWE HOLDINGS LLC</span></div>
  </section>
  <section class="card card--red" style="left:605px; top:21px;">
    <p class="name centered">Dean R Vossler</p>
    <p class="rule-title">CHIEF EXECUTIVE MANAGER</p>
    <p class="contact centered">412 N Ridgeview Lane #118, Linden Falls, Il 60412<br>Phone: (555) 555-0148<br>Email: dean.vossler@marloweholdingsffl.com</p>
    <p class="contact centered license">KPV FFL LICENSE NUMBER: 5-21-XXX-XX-XX-04519</p>
  </section>

  <!-- Row 2 -->
  <section class="card" style="left:28px; top:418px;">
    <div class="brand"><span class="brand__dot"></span><span class="brand__name">MARLOWE HOLDINGS LLC</span></div>
  </section>
  <section class="card card--band" style="left:610px; top:416px;">
    <p class="name centered">Dean R Vossler</p>
    <p class="title centered">Chief Executive Manager</p>
    <p class="contact centered address">412 N Ridgeview Lane #118<br>Linden Falls, Il 60412<br>Phone: (555) 555-0148<br>dean.vossler@marloweholdingsffl.com</p>
    <svg class="band" viewBox="0 0 572 349" aria-hidden="true">
      <path d="M0 252 L140 250 A145 93 0 0 0 430 250 L572 248 L572 349 L0 349 Z" fill="var(--brand-red)"/>
      <path d="M0 252 L140 249 L141 255 A145 93 0 0 0 429 255 L432 247 L572 248" fill="none" stroke="var(--ink)" stroke-width="3"/>
    </svg>
    <p class="contact centered license">KPV FFL LICENSE NUMBER:<br>5-21-XXX-XX-XX-04519</p>
  </section>

  <!-- Row 3 -->
  <section class="card" style="left:28px; top:791px;">
    <div class="brand"><span class="brand__dot"></span><span class="brand__name">MARLOWE HOLDINGS LLC</span></div>
  </section>
  <section class="card card--offset" style="left:607px; top:792px;">
    <p class="name">Dean R Vossler</p>
    <p class="title">Chief Executive Manager</p>
    <p class="contact address">412 N Ridgeview Lane #118<br>Linden Falls, Il 60412<br>Phone: (555) 555-0148<br>dean.vossler@marloweholdingsffl.com</p>
    <span class="accent-line"></span>
    <p class="contact license">KPV FFL LICENSE NUMBER: 5-21-XXX-XX-XX-04519</p>
    <div class="decor-area" role="img" aria-label="Large cropped brand emblem decoration in red"></div>
  </section>

</div>
</body>
</html>
```